Flyer Design / Authenticity Certificate - Art Work

Looking for a design of a "Authenticity Certificate" - flyer, that will include some basic company info like logo etc, and allow our in house artist to sign and authenticate before it is applied the reverse of one of the paintings we will sell. Linked with our online sales website - "Copper Hollow Canvases", where we recreate one off oil paintings from digital photographs. Our business logo should be incorporated in the design, along with a section for "Artisit Name" "Artisit Signature" "Ref Code"
Updates

Hi.. Sorry I should have added the size we need - please design accordingly to A6. Thanks.

Industry/Entity Type

It Company

Font styles to use
Serif
Script

Colors

Designer to choose colors to be used in the design.

Requirements
Must have
• Company logo
• Area for artist to print and sign
• Area for a reference
Nice to have
• must use the logo, maybe incorporate a "seal" icon, like what was used as a wax seal on older style documents

```html
<!DOCTYPE html>
<html lang="en">
<head>
<meta charset="utf-8">
<title>Authenticity Certificate – Copper Hollow Canvases</title>
<link rel="stylesheet" href="https://fonts.googleapis.com/css2?family=Pinyon+Script&family=Tinos:ital@0;1&display=swap">
<style>
  :root {
    --page: #ffffff;
    --sheet: #fdfdfd;
    --ink: #1c1c1c;
    --rule: #9c9c9c;
    --frame-line: #b5b5b5;
    --ornament-light: #e2e2e2;
    --ornament-mid: #cdcdcd;
    --brand: #2b2b2b;
    --seal: #b3121c;
    --seal-dark: #8e0d15;
    --twine: #d9b27c;
  }
  html, body {
    margin: 0;
    padding: 0;
    width: 1200px;
    height: 1200px;
    overflow: hidden;
    background: var(--page);
  }
  .canvas {
    position: relative;
    width: 1200px;
    height: 1200px;
    font-family: "Tinos", "Times New Roman", serif;
    color: var(--ink);
  }
  .certificate {
    position: absolute;
    left: 37px;
    top: 194px;
    width: 1127px;
    height: 803px;
    box-sizing: border-box;
    border: 1px solid #6e6e6e;
    background: var(--sheet);
  }
  .ornament-border {
    position: absolute;
    left: 23px;
    top: 22px;
    width: 1076px;
    height: 758px;
    box-sizing: border-box;
    border: 35px solid var(--ornament-mid);
    border-image: linear-gradient(135deg, var(--ornament-mid), var(--ornament-light), var(--ornament-mid)) 1;
  }
  .inner-frame {
    position: absolute;
    left: 65px;
    top: 64px;
    width: 994px;
    height: 672px;
    box-sizing: border-box;
    border: 1px solid var(--frame-line);
  }
  .inner-frame::after {
    content: "";
    position: absolute;
    inset: 7px;
    border: 1px solid var(--frame-line);
  }
  .brand {
    position: absolute;
    left: 0;
    right: 0;
    top: 111px;
    text-align: center;
  }
  .brand-mark {
    display: block;
    width: 118px;
    height: 118px;
    margin: 0 auto;
    border-radius: 50%;
    background: var(--brand);
  }
  .brand-name {
    margin: 18px 0 0;
    font-size: 27px;
    line-height: 1;
    letter-spacing: 1px;
    color: var(--brand);
    font-weight: 400;
  }
  .title {
    position: absolute;
    left: 0;
    right: 0;
    top: 312px;
    margin: 0;
    text-align: center;
    font-family: "Pinyon Script", cursive;
    font-weight: 400;
    font-size: 78px;
    line-height: 1.2;
    color: var(--ink);
  }
  .description {
    position: absolute;
    left: 0;
    right: 0;
    top: 442px;
    margin: 0;
    text-align: center;
    font-style: italic;
    font-size: 30px;
    line-height: 38px;
    color: var(--ink);
  }
  .fields {
    position: absolute;
    left: 129px;
    top: 649px;
    display: flex;
    gap: 24px;
  }
  .field {
    width: 236px;
    border-top: 1px solid var(--rule);
    text-align: center;
    padding-top: 12px;
    font-size: 22.5px;
    color: var(--ink);
  }
  .seal {
    position: absolute;
    left: 919px;
    top: 558px;
    width: 84px;
    height: 152px;
    border-radius: 14px;
    background: linear-gradient(180deg, var(--twine) 0%, var(--seal) 35%, var(--seal-dark) 65%, var(--twine) 100%);
  }
</style>
</head>
<body>
<div class="canvas">
  <section class="certificate">
    <div class="ornament-border" role="img" aria-label="Ornamental filigree scrollwork border framing the certificate"></div>

    <div class="inner-frame"></div>

    <header class="brand">
      <span class="brand-mark"></span>
      <p class="brand-name">COPPER HOLLOW CANVASES</p>
    </header>

    <h1 class="title">Authenticity Certificate</h1>

    <p class="description">[Enter description Enter description Enter description<br>Enter description Enter description]</p>

    <div class="fields">
      <div class="field">Ref Code</div>
      <div class="field">Artist Name</div>
      <div class="field">Artist Signature</div>
    </div>

    <div class="seal" role="img" aria-label="Red wax seal with a twine loop"></div>
  </section>
</div>
</body>
</html>
```